Bref créative
RVM Ltd stationary set
letterhead, business cards, envelopes
I need single sided standard sized Business Card [3.5" x 2"]
Designer's choice
Professional
Martin K. Dobbs
Registered Patent Attorney
82 E. Parkhill Street
Suite 4785
Chicago, IL 60417
martindobbs@claimwisp.com
www.claimwisp.com
A version of the "old" letterhead can be downloaded here: https://claimwisp.filevault-example.net/shared/q8tr2m4vbnxwpla7c3dk
RVM logo (ai format)

```html
<!DOCTYPE html>
<html lang="en">
<head>
<meta charset="utf-8">
<title>RVM Ltd Stationery Set</title>
<link href="https://fonts.googleapis.com/css2?family=Libre+Baskerville&family=Open+Sans:wght@400;600&display=swap" rel="stylesheet">
<style>
  :root {
    --backdrop: #cbcbcb;
    --paper: #ffffff;
    --edge: #b4b4b4;
    --brand-blue: #2a55a0;
    --ink: #4a4a4a;
    --band-text: #ffffff;
    --flap-line: #c9c9c9;
  }
  * { margin: 0; padding: 0; box-sizing: border-box; }
  html, body { width: 1200px; height: 684px; overflow: hidden; }
  body {
    background: var(--backdrop);
    font-family: "Open Sans", Arial, sans-serif;
    color: var(--ink);
    position: relative;
  }
  .sheet {
    position: absolute;
    background: var(--paper);
    box-shadow: 0 0 0 1px var(--edge);
    overflow: hidden;
  }
  .brand {
    position: absolute;
    display: flex;
    align-items: center;
    gap: 8px;
  }
  .brand-square {
    background: var(--brand-blue);
    flex: none;
  }
  .brand-name {
    font-family: "Libre Baskerville", Georgia, serif;
    color: var(--brand-blue);
    letter-spacing: 1px;
    white-space: nowrap;
  }
  .contact {
    position: absolute;
    font-size: 6px;
    line-height: 9px;
    color: var(--ink);
    white-space: nowrap;
  }
  .contact b { color: var(--brand-blue); font-weight: 600; }
  .band {
    position: absolute;
    left: 0; right: 0;
    background: var(--brand-blue);
    color: var(--band-text);
    font-size: 6px;
    line-height: 1;
    display: flex;
    align-items: center;
    padding-left: 10px;
  }

  /* Letterhead */
  .letterhead { left: 192px; top: 58px; width: 384px; height: 595px; }
  .letterhead .brand { left: 24px; top: 14px; }
  .letterhead .brand-square { width: 30px; height: 30px; }
  .letterhead .brand-name { font-size: 13px; }
  .letterhead .contact { left: 24px; top: 548px; }
  .letterhead .band { bottom: 0; height: 11px; }

  /* Business card */
  .business-card { left: 29px; top: 281px; width: 264px; height: 158px; }
  .business-card .brand { left: 14px; top: 12px; }
  .business-card .brand-square { width: 22px; height: 22px; }
  .business-card .brand-name { font-size: 10px; }
  .card-person { position: absolute; left: 14px; top: 70px; }
  .card-person .name { font-size: 7px; font-weight: 600; color: var(--brand-blue); line-height: 9px; }
  .card-person .title { font-size: 6px; line-height: 8px; }
  .business-card .contact { left: 14px; top: 100px; font-size: 5px; line-height: 7px; }
  .business-card .band { bottom: 12px; height: 14px; padding-left: 14px; }

  /* Envelope back */
  .envelope-back { left: 636px; top: 108px; width: 535px; height: 197px; }
  .envelope-back svg { position: absolute; left: 0; top: 0; }
  .envelope-back .brand-square {
    position: absolute; left: 254px; top: 20px; width: 28px; height: 28px;
  }

  /* Envelope front */
  .envelope-front { left: 636px; top: 377px; width: 535px; height: 278px; }
  .envelope-front .brand { left: 30px; top: 28px; }
  .envelope-front .brand-square { width: 30px; height: 30px; }
  .envelope-front .brand-name { font-size: 13px; }
  .envelope-front .contact { left: 30px; top: 181px; }
  .envelope-front .band { bottom: 12px; height: 11px; }
</style>
</head>
<body>

  <section class="sheet letterhead" aria-label="Letterhead">
    <div class="brand">
      <span class="brand-square"></span>
      <span class="brand-name">RVM LTD.</span>
    </div>
    <div class="contact">
      <div><b>E:</b> martindobbs@claimwisp.com</div>
      <div><b>P:</b> 312 555 0148 | <b>F:</b> 312 555 0192 | <b>M:</b> 312 555 0173</div>
      <div><b>A:</b> 82 E. Parkhill Street Suite 4785 Chicago, IL 60417</div>
    </div>
    <div class="band">www.claimwisp.com</div>
  </section>

  <section class="sheet business-card" aria-label="Business card">
    <div class="brand">
      <span class="brand-square"></span>
      <span class="brand-name">RVM LTD.</span>
    </div>
    <div class="card-person">
      <div class="name">Martin K. Dobbs</div>
      <div class="title">Registered Patent Attorney</div>
    </div>
    <div class="contact">
      <div><b>E:</b> martindobbs@claimwisp.com</div>
      <div><b>P:</b> 312 555 0148 | <b>F:</b> 312 555 0192 | <b>M:</b> 312 555 0173</div>
      <div><b>A:</b> 82 E. Parkhill Street Suite 4785 Chicago, IL 60417</div>
    </div>
    <div class="band">www.claimwisp.com</div>
  </section>

  <section class="sheet envelope-back" aria-label="Envelope back">
    <svg width="535" height="197" viewBox="0 0 535 197" aria-hidden="true">
      <path d="M0 0 L230 70 Q267 82 304 70 L535 0" fill="none" stroke="var(--flap-line)" stroke-width="1"/>
      <path d="M0 197 L200 95 Q267 70 334 95 L535 197" fill="none" stroke="var(--flap-line)" stroke-width="1"/>
    </svg>
    <span class="brand-square"></span>
  </section>

  <section class="sheet envelope-front" aria-label="Envelope front">
    <div class="brand">
      <span class="brand-square"></span>
      <span class="brand-name">RVM LTD.</span>
    </div>
    <div class="contact">
      <div><b>E:</b> martindobbs@claimwisp.com</div>
      <div><b>P:</b> 312 555 0148 | <b>F:</b> 312 555 0192 | <b>M:</b> 312 555 0173</div>
      <div><b>A:</b> 82 E. Parkhill Street Suite 4785 Chicago, IL 60417</div>
    </div>
    <div class="band">www.claimwisp.com</div>
  </section>

</body>
</html>
```